Marwick Dance Festival Association

We need a design for a pull up banner for the dance festival. The festival takes place every year and aims to encourage dancers in the local area to perform. Dancers are judged on their performance the genres include ballet, jazz, tap and hip hop.
The banner will be 850mm x 2000mm. .ai files will be required.
We have no current logo - a new logo can be included as part of the design. Please do not include the year as it is a banner we would use over several years. We are looking for bright attractive colours - preferably with a reflection of the different genres. One suggestion was to include silhouettes of the different genres (in colour) but other suggestions are welcome.

```html
<!DOCTYPE html>
<html lang="en">
<head>
<meta charset="utf-8">
<title>Marwick Dance Festival – Pull-up Banners</title>
<link href="https://fonts.googleapis.com/css2?family=Krona+One&display=swap" rel="stylesheet">
<style>
  :root {
    --ink: #0b0b0b;
    --paper: #ffffff;
    --frame: #b9b9b9;
    --gold: #f2b90f;
    --cool-green: 60, 170, 70;
    --cool-blue: 70, 110, 200;
    --cool-teal: 80, 190, 200;
    --warm-red: 235, 70, 40;
    --warm-orange: 245, 140, 60;
    --warm-yellow: 235, 200, 110;
    --dancer-cool: #6fb2d8;
    --dancer-warm: #e6c877;
    --font-display: "Krona One", "Arial Black", sans-serif;
  }
  * { box-sizing: border-box; margin: 0; padding: 0; }
  html, body { width: 1200px; height: 900px; overflow: hidden; background: var(--paper); }
  .canvas { position: relative; width: 1200px; height: 900px; font-family: var(--font-display); color: var(--ink); }

  .banner {
    position: absolute; top: 53px; width: 337px; height: 792px;
    background: var(--paper); border: 1px solid var(--frame); overflow: hidden;
  }
  .banner--cool { left: 53px; }
  .banner--warm { left: 810px; }

  .petals { position: absolute; }
  .petals--top { left: 0; top: 0; width: 290px; height: 340px; }
  .petals--bottom { right: 0; bottom: 0; width: 320px; height: 320px; }
  .banner--cool .petals--top {
    background:
      radial-gradient(ellipse 70% 60% at 20% 20%, rgba(var(--cool-green), .75), rgba(var(--cool-blue), .45) 55%, rgba(255,255,255,0) 100%);
  }
  .banner--cool .petals--bottom {
    background:
      radial-gradient(ellipse 75% 70% at 80% 85%, rgba(var(--cool-green), .7), rgba(var(--cool-blue), .45) 55%, rgba(255,255,255,0) 100%);
  }
  .banner--warm .petals--top {
    width: 320px; height: 360px;
    background:
      radial-gradient(ellipse 70% 60% at 25% 20%, rgba(var(--warm-red), .7), rgba(var(--warm-orange), .4) 55%, rgba(255,255,255,0) 100%);
  }
  .banner--warm .petals--bottom {
    width: 337px;
    background:
      radial-gradient(ellipse 75% 70% at 60% 85%, rgba(var(--warm-red), .75), rgba(var(--warm-orange), .4) 55%, rgba(255,255,255,0) 100%);
  }

  .dancer { position: absolute; border-radius: 45% 55% 40% 60%; opacity: .85; }
  .banner--cool .dancer { background: var(--dancer-cool); }
  .banner--warm .dancer { background: var(--dancer-warm); }
  .banner--cool .dancer--upper { left: 225px; top: 130px; width: 95px; height: 100px; }
  .banner--cool .dancer--lower { left: 28px; top: 460px; width: 95px; height: 150px; }
  .banner--warm .dancer--upper { left: 200px; top: 148px; width: 100px; height: 100px; }
  .banner--warm .dancer--lower { left: 28px; top: 470px; width: 85px; height: 165px; }

  .association-mark {
    position: absolute; left: 0; width: 100%;
    display: flex; align-items: center; justify-content: center; gap: 5px;
    font-size: 6px; letter-spacing: .02em; color: var(--ink);
  }
  .association-mark__dot { width: 12px; height: 12px; border-radius: 50%; background: var(--ink); flex: none; }
  .banner--cool .association-mark--top { top: 29px; }
  .banner--cool .association-mark--bottom { top: 726px; }
  .banner--warm .association-mark--top { top: 29px; }
  .banner--warm .association-mark--bottom { top: 716px; }

  .title {
    position: absolute; left: 0; width: 100%;
    display: flex; flex-direction: column; align-items: center; text-align: center;
  }
  .title__place, .title__kind { font-size: 15px; letter-spacing: .42em; padding-left: .42em; line-height: 1; }
  .title__word { display: flex; flex-direction: column; align-items: center; }
  .title__word span { font-size: 78px; line-height: 86px; display: block; }

  .banner--cool .title { top: 121px; }
  .banner--cool .title__word { margin-top: 19px; }
  .banner--cool .title__kind { margin-top: 23px; }
  .banner--warm .title { top: 104px; }
  .banner--warm .title__word { margin-top: 18px; }
  .banner--warm .title__kind { margin-top: 20px; }

  .brand-mark {
    position: absolute; left: 420px; top: 300px; width: 360px;
    display: flex; flex-direction: column; align-items: center; gap: 22px;
  }
  .brand-mark__disc { width: 170px; height: 170px; border-radius: 50%; background: var(--gold); }
  .brand-mark__name { font-size: 19px; line-height: 1.45; text-align: center; color: var(--ink); letter-spacing: .03em; }
</style>
</head>
<body>
<main class="canvas">

  <section class="banner banner--cool" aria-label="Pull-up banner, cool colourway">
    <div class="petals petals--top" role="img" aria-label="Overlapping translucent green and blue petal shapes"></div>
    <div class="petals petals--bottom" role="img" aria-label="Overlapping translucent green and blue petal shapes"></div>
    <div class="dancer dancer--upper" role="img" aria-label="Teal silhouette of a leaping dancer"></div>
    <div class="dancer dancer--lower" role="img" aria-label="Blue silhouette of a jumping hip hop dancer"></div>

    <div class="association-mark association-mark--top"><span class="association-mark__dot"></span>Marwick Dance Festival Association</div>

    <h1 class="title">
      <span class="title__place">MARWICK</span>
      <span class="title__word"><span>D</span><span>A</span><span>N</span><span>C</span><span>E</span></span>
      <span class="title__kind">FESTIVAL</span>
    </h1>

    <div class="association-mark association-mark--bottom"><span class="association-mark__dot"></span>Marwick Dance Festival Association</div>
  </section>

  <div class="brand-mark">
    <span class="brand-mark__disc"></span>
    <p class="brand-mark__name">Marwick Dance<br>Festival Association</p>
  </div>

  <section class="banner banner--warm" aria-label="Pull-up banner, warm colourway">
    <div class="petals petals--top" role="img" aria-label="Overlapping translucent red and orange petal shapes"></div>
    <div class="petals petals--bottom" role="img" aria-label="Overlapping translucent red and orange petal shapes"></div>
    <div class="dancer dancer--upper" role="img" aria-label="Golden silhouette of a leaping dancer"></div>
    <div class="dancer dancer--lower" role="img" aria-label="Golden silhouette of a jumping hip hop dancer"></div>

    <div class="association-mark association-mark--top"><span class="association-mark__dot"></span>Marwick Dance Festival Association</div>

    <h2 class="title">
      <span class="title__place">MARWICK</span>
      <span class="title__word"><span>D</span><span>A</span><span>N</span><span>C</span><span>E</span></span>
      <span class="title__kind">FESTIVAL</span>
    </h2>

    <div class="association-mark association-mark--bottom"><span class="association-mark__dot"></span>Marwick Dance Festival Association</div>
  </section>

</main>
</body>
</html>
```